Weihnachtskarten-Design
Zielgruppe
Rechtsanwaltskanzlei
Aufgabenstellung
Es soll eine kreative Weihnachtskarte werden / das corporate Design der Kanzlei sollte beachtet werden (siehe www.kanzlei-drbrammel.de). Die Weihnachtskarte soll 4 Seiten umfassen (also eine aufklappbare Weihnachtskarte).

```html
<!DOCTYPE html>
<html lang="de">
<head>
<meta charset="utf-8">
<title>Weihnachtskarte – Kanzlei Brammel</title>
<link rel="stylesheet" href="https://fonts.googleapis.com/css2?family=Merriweather:wght@400;700;900&display=swap">
<style>
  :root {
    --backdrop: #cbd3e1;
    --paper: #ffffff;
    --navy: #0b2146;
    --navy-soft: #1c3563;
    --ink-muted: #5a6785;
    --shadow: rgba(20, 35, 70, 0.18);
    --serif: "Merriweather", Georgia, serif;
  }
  * { box-sizing: border-box; margin: 0; padding: 0; }
  html, body {
    width: 1200px; height: 800px; overflow: hidden;
    background: var(--backdrop);
    font-family: var(--serif);
  }
  .card-spread {
    position: absolute; top: 225px; left: 25px;
    display: flex; gap: 50px;
  }
  .card-page {
    position: relative; width: 350px; height: 350px;
    background: var(--paper);
    box-shadow: 0 6px 18px var(--shadow);
    overflow: hidden;
  }
  .card-page--dark {
    background: radial-gradient(circle at 40% 45%, var(--navy-soft) 0%, var(--navy) 70%);
  }
  .ornament-string {
    position: absolute; left: 174px; top: 0; width: 1.5px; height: 80px;
    background: var(--navy);
  }
  .card-page--dark .ornament-string { background: var(--paper); }
  .ornament {
    position: absolute; left: 75px; top: 70px; width: 200px; height: 200px;
  }
  .ornament-wreath { position: absolute; inset: 0; }
  .ornament-window {
    position: absolute; left: 34px; top: 34px; width: 132px; height: 132px;
    border-radius: 50%; background: var(--paper);
    box-shadow: inset 0 3px 8px var(--shadow), 0 0 0 5px var(--paper);
    display: flex; flex-direction: column; align-items: center; justify-content: center;
    text-align: center; color: var(--navy);
  }
  .greeting-main {
    font-weight: 900; font-size: 15px; line-height: 1.1; letter-spacing: 0.5px;
  }
  .greeting-rule {
    width: 92px; margin: 5px 0 4px; border-top: 1px dotted var(--ink-muted);
  }
  .greeting-sub { font-weight: 400; font-size: 9px; }
  .firm-name {
    position: absolute; right: 18px; bottom: 18px;
    font-weight: 700; font-size: 12px; letter-spacing: 0.3px; line-height: 1;
    color: var(--navy);
  }
  .card-page--dark .firm-name { color: var(--paper); }
  .night-dots { position: absolute; inset: 0; }
</style>
</head>
<body>
  <main class="card-spread">

    <section class="card-page card-page--front">
      <div class="ornament-string"></div>
      <div class="ornament">
        <svg class="ornament-wreath" viewBox="0 0 200 200" role="img" aria-label="Kranz aus dunkelblauen Schneeflocken rund um die Weihnachtskugel">
          <circle cx="100" cy="100" r="84" fill="none" stroke="var(--navy)" stroke-width="30" opacity="0.85"/>
        </svg>
        <div class="ornament-window">
          <p class="greeting-main">MERRY<br>CHRISTMAS</p>
          <span class="greeting-rule"></span>
          <p class="greeting-sub">&amp; Happy New Year</p>
        </div>
      </div>
      <p class="firm-name">Kanzlei Brammel</p>
    </section>

    <section class="card-page card-page--dark">
      <svg class="night-dots" viewBox="0 0 350 350" aria-hidden="true">
        <g fill="#ffffff" opacity="0.12">
          <circle cx="40" cy="120" r="1.5"/><circle cx="300" cy="60" r="1.5"/>
          <circle cx="60" cy="290" r="2"/><circle cx="290" cy="250" r="1.5"/>
          <circle cx="120" cy="40" r="1"/><circle cx="240" cy="310" r="1"/>
          <circle cx="30" cy="210" r="6" opacity="0.5"/><circle cx="320" cy="170" r="8" opacity="0.4"/>
        </g>
      </svg>
      <div class="ornament-string"></div>
      <div class="ornament">
        <svg class="ornament-wreath" viewBox="0 0 200 200" role="img" aria-label="Kranz aus weißen Schneeflocken rund um die Weihnachtskugel">
          <circle cx="100" cy="100" r="84" fill="none" stroke="#ffffff" stroke-width="30" opacity="0.85"/>
        </svg>
        <div class="ornament-window">
          <p class="greeting-main">MERRY<br>CHRISTMAS</p>
          <span class="greeting-rule"></span>
          <p class="greeting-sub">&amp; Happy New Year</p>
        </div>
      </div>
      <p class="firm-name">Kanzlei Brammel</p>
    </section>

    <section class="card-page card-page--inside">
      <div class="ornament-string"></div>
      <div class="ornament">
        <svg class="ornament-wreath" viewBox="0 0 200 200" role="img" aria-label="Kranz aus dunkelblauen Schneeflocken rund um ein leeres Textfeld">
          <circle cx="100" cy="100" r="84" fill="none" stroke="var(--navy)" stroke-width="30" opacity="0.85"/>
        </svg>
        <div class="ornament-window"></div>
      </div>
      <p class="firm-name">Kanzlei Brammel</p>
    </section>

  </main>
</body>
</html>
```